Voravolt Sports Performance Poster

We are in need of a poster for our upcoming summer Sports Performance Program during June and July.
This program caters to youth and teen athletes playing volleyball, soccer, and basketball.
Please see attached word document with program details for the poster.

MUST HAVES:
- Size needed 11x17 with bleeding for printing
- .PSD File Format WITH LAYERS (CS3 Compatible - Fonts included)*** A MUST
- Use Voravolt Bootcamps Logo
- Use Information in the attached word doc

Requirements
Must have
• - Size needed 11x17 with bleeding for printing
• - .PSD File Format WITH LAYERS (CS3 Compatible - Fonts included)*** A MUST
• - Use Voravolt Bootcamps Logo
• - Use Information in the attached word doc

```html
<!DOCTYPE html>
<html lang="en">
<head>
<meta charset="utf-8">
<title>Voravolt Sports Performance Program</title>
<link rel="stylesheet" href="https://fonts.googleapis.com/css2?family=Source+Sans+3:wght@400;600;700;800&display=swap">
<style>
  :root {
    --maroon-deep: #2a0606;
    --maroon: #5a0d0a;
    --ember: #8a2410;
    --orange: #f0a05a;
    --blue: #1f62ad;
    --blue-deep: #123f7c;
    --bubble: #143567;
    --white: #ffffff;
    --gold: #f4c873;
    --logo-bg: #e9e6df;
    --logo-ink: #1b1b1b;
  }
  * { margin: 0; padding: 0; box-sizing: border-box; }
  html, body { width: 776px; height: 1200px; overflow: hidden; background: var(--maroon-deep); }
  body { font-family: "Source Sans 3", "Source Sans Pro", sans-serif; color: var(--white); }

  .poster { position: relative; width: 776px; height: 1200px; overflow: hidden;
    background: radial-gradient(ellipse at 45% 22%, var(--ember) 0%, var(--maroon) 45%, var(--maroon-deep) 100%); }

  .hero-photo { position: absolute; left: 0; top: 0; width: 776px; height: 620px;
    background: radial-gradient(ellipse 260px 320px at 260px 200px, rgba(200,80,30,0.35), transparent 70%); }

  .brand-mark { position: absolute; left: 247px; top: 31px; width: 275px; height: 89px;
    background: var(--logo-bg); border: 3px solid var(--logo-ink); border-radius: 4px;
    display: flex; align-items: center; justify-content: center; gap: 10px; }
  .brand-mark .dot { width: 16px; height: 16px; background: var(--logo-ink); }
  .brand-mark .name { font-weight: 800; font-size: 25px; color: var(--logo-ink); text-transform: uppercase; letter-spacing: 0.5px; }

  .presenter { position: absolute; top: 128px; width: 100%; text-align: center;
    font-weight: 600; font-size: 27px; letter-spacing: 2px; color: var(--orange); }

  .title { position: absolute; left: 0; width: 100%; text-align: center; font-weight: 800; line-height: 1; }
  .title.sports { top: 156px; font-size: 134px; letter-spacing: 3px; }
  .title.performance { top: 270px; font-size: 100px; }
  .title.program { top: 352px; font-size: 132px; letter-spacing: 1px; }

  .blue-field { position: absolute; left: 0; top: 0; width: 776px; height: 1200px; }

  .athletes-photo { position: absolute; left: 470px; top: 565px; width: 306px; height: 635px;
    border-radius: 140px 0 0 0;
    background: linear-gradient(180deg, #2f6fbf 0%, #3a5f94 35%, #6e6a6a 70%, #2a3550 100%); }

  .pillars { position: absolute; top: 548px; left: 150px; font-weight: 700; font-size: 34px; letter-spacing: 0.5px; }

  .ages { position: absolute; left: 38px; top: 650px; width: 450px; text-align: center;
    font-weight: 600; font-size: 41px; line-height: 49px; }
  .dates { position: absolute; left: 158px; top: 812px; font-weight: 600; font-size: 26px; line-height: 37px; }
  .dates sup { font-size: 15px; }

  .schedule { position: absolute; left: 65px; top: 972px; font-weight: 600; font-size: 22px; }
  .schedule .days { margin-bottom: 10px; }
  .schedule .row { display: flex; line-height: 31.5px; }
  .schedule .row span:first-child { width: 56px; }
  .schedule .row span:nth-child(2) { width: 30px; }
  .capacity { position: absolute; left: 65px; top: 1118px; font-weight: 600; font-size: 22px; }
  .capacity .accent { color: var(--gold); }
  .pricing { position: absolute; left: 65px; top: 1153px; font-weight: 600; font-size: 16px; }
</style>
</head>
<body>
<main class="poster">
  <div class="hero-photo" role="img" aria-label="Blurred action photo of an athlete in warm red and orange tones"></div>

  <div class="brand-mark"><span class="dot"></span><span class="name">Voravolt Bootcamps</span></div>
  <p class="presenter">Voravolt’s</p>
  <h1>
    <span class="title sports">SPORTS</span>
    <span class="title performance">PERFORMANCE</span>
    <span class="title program">PROGRAM</span>
  </h1>

  <svg class="blue-field" viewBox="0 0 776 1200" aria-hidden="true">
    <defs>
      <linearGradient id="fieldGrad" x1="0" y1="0" x2="0" y2="1">
        <stop offset="0" stop-color="#2468b5"/>
        <stop offset="1" stop-color="#174f92"/>
      </linearGradient>
    </defs>
    <path d="M0 620 Q388 430 776 620 L776 1200 L0 1200 Z" fill="url(#fieldGrad)"/>
    <ellipse cx="263" cy="766" rx="226" ry="176" fill="#143567"/>
    <polygon points="398,822 430,816 414,836" fill="#e3a25e"/>
    <polygon points="372,832 384,838 372,844" fill="#ffffff"/>
    <polygon points="392,856 408,850 398,870" fill="#3a7ad0"/>
    <polygon points="378,858 388,864 378,868" fill="#ffffff"/>
    <polygon points="386,884 410,880 402,900" fill="#e3a25e"/>
    <polygon points="420,868 436,862 430,880" fill="#2f6fbf"/>
    <polygon points="420,978 432,982 424,990" fill="#e3a25e"/>
    <polygon points="452,968 462,972 452,980" fill="#3a7ad0"/>
  </svg>

  <div class="athletes-photo" role="img" aria-label="Photo of three young athletes running, one dribbling a basketball"></div>

  <p class="pillars">SPEED | AGILITY | POWER</p>

  <div class="ages">AGES 8-17<br>YOUTH AND<br>TEEN PROGRAMS</div>
  <div class="dates">June 5<sup>th</sup> – 30<sup>th</sup><br>&nbsp;July 5<sup>th</sup> – 31<sup>st</sup></div>

  <div class="schedule">
    <p class="days">Monday | Wednesday | Friday</p>
    <p class="row"><span>Youth</span><span>–</span><span>9:30-10:30am</span></p>
    <p class="row"><span>Teen</span><span>–</span><span>10:30-11:30am</span></p>
    <p class="row"><span>Teen</span><span>–</span><span>3:30-4:30pm</span></p>
  </div>
  <p class="capacity"><span class="accent">Limited Space</span> – 15 spots per time track</p>
  <p class="pricing">$119 per month or $199 for both months</p>
</main>
</body>
</html>
```